Sliding banner

I need three sliding banners designed for my website tillvane.co.za - please take a look at the existing banner format.

The products items on the banner can be any product that is on the website - the size of the banner must remain the same - the design project is only for the sliding banner.

Regards

```html
<!DOCTYPE html>
<html lang="en">
<head>
<meta charset="utf-8">
<title>tillvane.co.za – Sliding banners</title>
<link rel="stylesheet" href="https://fonts.googleapis.com/css2?family=Open+Sans:ital,wght@0,400;0,600;1,400&display=swap">
<style>
  :root {
    --page-bg: #000000;
    --banner-start: #e4e4e4;
    --banner-end: #ffffff;
    --accent: #29a9e1;
    --text-dark: #3a3a3a;
    --text-muted: #a8a8a8;
    --button-text: #ffffff;
    --icon-ring: #d4d4d4;
    --rule: #cfcfcf;
  }
  * { margin: 0; padding: 0; box-sizing: border-box; }
  html, body {
    width: 1108px;
    height: 1200px;
    overflow: hidden;
    background: var(--page-bg);
    font-family: "Open Sans", Arial, sans-serif;
  }
  .slides {
    position: relative;
    width: 1108px;
    height: 1200px;
  }
  .banner {
    position: absolute;
    left: 12px;
    width: 1080px;
    height: 369px;
    background: linear-gradient(90deg, var(--banner-start) 0%, #f7f7f7 35%, var(--banner-end) 60%);
    overflow: hidden;
  }
  .banner--cables { top: 28px; border-bottom: 3px solid var(--rule); }
  .banner--battery { top: 420px; }
  .banner--car { top: 812px; }

  .banner__title {
    position: absolute;
    left: 147px;
    top: 72px;
    font-size: 38px;
    font-weight: 600;
    letter-spacing: -0.5px;
    color: var(--accent);
    line-height: 1;
    white-space: nowrap;
  }
  .banner__text {
    position: absolute;
    left: 147px;
    top: 121px;
    font-size: 15px;
    font-weight: 600;
    letter-spacing: -0.3px;
    line-height: 18px;
    color: var(--text-dark);
  }
  .banner__button {
    position: absolute;
    left: 148px;
    top: 218px;
    width: 204px;
    height: 51px;
    background: var(--accent);
    color: var(--button-text);
    font-size: 24px;
    font-weight: 600;
    letter-spacing: -0.8px;
    display: flex;
    align-items: center;
    justify-content: center;
    text-decoration: none;
  }
  .banner__note {
    position: absolute;
    left: 148px;
    top: 294px;
    display: flex;
    align-items: center;
    gap: 10px;
    font-size: 15px;
    font-style: italic;
    letter-spacing: -0.4px;
    color: var(--text-muted);
    white-space: nowrap;
  }
  .banner__note svg { flex: none; }
  .banner__product {
    position: absolute;
    border-radius: 6px;
  }
  .banner--cables .banner__product {
    left: 648px; top: 46px; width: 194px; height: 256px;
    background: linear-gradient(180deg, #f2f2f2, #e2e2e2);
  }
  .banner--battery .banner__product {
    left: 588px; top: 65px; width: 323px; height: 221px;
    background: linear-gradient(135deg, #4a4a4a 0%, #8a8a8a 55%, #e8e8e8 100%);
  }
  .banner--car .banner__product {
    left: 625px; top: 102px; width: 263px; height: 175px;
    background: linear-gradient(180deg, #f4f4f4, #d8d8d8);
  }
</style>
</head>
<body>
<main class="slides">

  <section class="banner banner--cables">
    <h2 class="banner__title">Vela Quickport</h2>
    <p class="banner__text">Charge/sync cables, now available for<br>your new Vela phone, Vela pod or Vela tab.</p>
    <a class="banner__button" href="#">GET IT NOW</a>
    <p class="banner__note">
      <svg width="22" height="22" viewBox="0 0 22 22" aria-hidden="true"><circle cx="11" cy="11" r="10" fill="var(--icon-ring)"/><circle cx="11" cy="11" r="4" fill="#ffffff"/></svg>
      Now available in the handy 1m or extra length 1.5m cable
    </p>
    <div class="banner__product" role="img" aria-label="White charge and sync cable with USB plug, coiled"></div>
  </section>

  <section class="banner banner--battery">
    <h2 class="banner__title">Rechargeable</h2>
    <p class="banner__text">Battery for powering up your<br>Mobile phone or Tablet when<br>you can't find a power outlet.</p>
    <a class="banner__button" href="#">GET IT NOW</a>
    <p class="banner__note">
      <svg width="22" height="22" viewBox="0 0 22 22" aria-hidden="true"><circle cx="11" cy="11" r="10" fill="var(--icon-ring)"/><circle cx="11" cy="11" r="4" fill="#ffffff"/></svg>
      Great for traveling, power outges, emergencies or other occasions
    </p>
    <div class="banner__product" role="img" aria-label="Tablet charging from a grey portable battery pack"></div>
  </section>

  <section class="banner banner--car">
    <h2 class="banner__title">Dual USB Car Charger</h2>
    <p class="banner__text">The Dual USB Car Charger that lets you<br>juice your mobile devices while on the<br>go. Charge your Mobile phone or<br>Tablet in your car at the same time.</p>
    <a class="banner__button" href="#">GET IT NOW</a>
    <p class="banner__note">
      <svg width="22" height="22" viewBox="0 0 22 22" aria-hidden="true"><circle cx="11" cy="11" r="10" fill="var(--icon-ring)"/><circle cx="11" cy="11" r="4" fill="#ffffff"/></svg>
      High quality 5v - 2amps - Fully charged in no time
    </p>
    <div class="banner__product" role="img" aria-label="White dual USB car charger plug"></div>
  </section>

</main>
</body>
</html>
```